Vextara website

Web design for small consulting firm
It can be simple, easy to find approach

The primary use is business to business for

a. people wanting to find out a bit more of us after receiving a business card
b. Search words to draw people from search engines to us

Target Market(s)

Senior staff of large companies, in their work capacity
MD / CEO / CFO , directors, etc.

Industry/Entity Type

Business

Colors
ffffff
f79020
faa54b
33a6d7

```html
<!DOCTYPE html>
<html lang="en">
<head>
<meta charset="utf-8">
<title>Vextara Insight</title>
<link rel="stylesheet" href="https://fonts.googleapis.com/css2?family=Arimo:wght@400;700&family=PT+Sans&display=swap">
<style>
:root{
  --orange:#f79020;
  --orange-deep:#f56a1e;
  --orange-soft:#faa54b;
  --blue:#33a6d7;
  --blue-dark:#0c2f86;
  --navy:#16267a;
  --white:#ffffff;
  --ink:#111111;
  --grey:#6e6e6e;
  --link:#1a44c8;
}
*{box-sizing:border-box;margin:0;padding:0}
html,body{width:1200px;height:1000px;overflow:hidden;background:#0a0a0a;font-family:"Arimo",Arial,sans-serif}
.page{position:absolute;left:200px;top:0;width:800px;height:1000px;background:var(--white)}
.wrap{position:absolute;left:59px;width:682px}
.top-strip{top:0;height:20px;background:var(--orange-deep)}
.header{top:20px;height:68px;background:linear-gradient(90deg,#fff 0%,#fff 18%,#f8c9a8 55%,#f59e73 100%);box-shadow:0 2px 6px rgba(0,0,0,.25)}
.brand{position:absolute;left:10px;top:14px;display:flex;align-items:center;gap:8px}
.brand-dot{width:14px;height:14px;border-radius:50%;background:var(--orange)}
.brand-name{font-size:34px;font-weight:700;color:#1c6fb3;letter-spacing:.5px}
.search{position:absolute;right:22px;top:10px;display:flex;align-items:center}
.search-field{width:106px;height:22px;border-radius:3px;background:#fbd7bf;border:1px solid #e89a6e;font-size:11px;line-height:20px;padding-left:6px;color:var(--ink)}
.search-btn{width:26px;height:24px;margin-left:1px;border-radius:3px;background:#fbd7bf;border:1px solid #e89a6e;display:flex;align-items:center;justify-content:center}
.nav{top:88px;height:32px;background:var(--blue);display:flex;align-items:center;justify-content:space-between;padding:0 16px 0 11px}
.nav a{color:var(--white);font-size:9.6px;font-weight:700;text-decoration:none;white-space:nowrap}
.nav a.active{background:var(--white);color:var(--orange-deep);border-radius:4px;padding:1px 6px}
.banner{top:120px;height:173px;background:linear-gradient(180deg,#1f57b8 0%,var(--blue-dark) 55%,var(--navy) 100%);overflow:hidden}
.banner-map{position:absolute;left:300px;top:0;width:330px;height:173px;background:radial-gradient(ellipse at 55% 45%,rgba(120,200,255,.55),rgba(40,110,210,.2) 60%,transparent 75%)}
.arrow{position:absolute;top:64px;width:30px;height:30px}
.arrow.prev{left:2px}.arrow.next{right:7px}
.services{position:absolute;left:30px;top:97px;list-style:none}
.services li{font-size:9.3px;font-weight:700;color:#4d63e8;height:13.2px;display:flex;align-items:center;gap:4px}
.services li::before{content:"";width:9px;height:9px;border-radius:50%;background:#8d99b8;border:2px solid #5f6c8f}
.welcome{top:303px}
.welcome h1{font-size:14px;color:var(--orange-deep);margin-left:5px;font-weight:700}
.welcome p{font-size:9.2px;line-height:13.3px;color:var(--ink);margin-left:5px;text-align:justify;margin-top:5px;hyphens:auto;-webkit-hyphens:auto}
.welcome p+p{margin-top:0;text-indent:28px}
.card{position:absolute;top:452px;width:207px}
.card-frame{height:220px;border:3px solid var(--grey);position:relative;background:linear-gradient(180deg,#f8f3ee,#efe6dc)}
.card-art{position:absolute;inset:0 0 17px 0;background:radial-gradient(ellipse at 50% 45%,#e2b63a 0%,#c8921c 22%,rgba(240,230,215,0) 55%)}
.card-caption{position:absolute;left:0;right:0;bottom:0;height:17px;background:var(--grey);color:var(--white);font-family:"PT Sans",sans-serif;font-size:15px;text-align:center;line-height:17px}
.card p{font-size:9.2px;line-height:13.4px;color:var(--ink);margin-top:14px;text-align:justify;width:218px;margin-left:-6px;hyphens:auto;-webkit-hyphens:auto}
.card a{font-size:9.2px;line-height:13.4px;color:var(--link);text-decoration:none;display:block;margin-left:-6px}
.feature{top:806px;height:95px;background:var(--blue);padding:4px}
.feature-art{position:absolute;left:4px;top:4px;width:170px;height:87px;background:linear-gradient(135deg,#fff 0%,#e6e6e6 60%,#f2c3b0 100%)}
.feature p{position:absolute;left:178px;top:7px;width:500px;font-size:9.2px;line-height:13.4px;color:var(--white);text-align:justify;height:80.4px;overflow:hidden;hyphens:auto;-webkit-hyphens:auto}
.footer{top:908px;height:92px;background:linear-gradient(180deg,#f86e1c,#f6741e);}
.foot-links{position:absolute;top:8px;list-style:none}
.foot-links li{font-size:9.5px;color:#c65a1a;line-height:13.3px}
.foot-links.one{left:21px}.foot-links.two{left:113px;top:10px}
.social{position:absolute;right:7px;top:12px;display:flex;gap:12px}
.social span{width:39px;height:39px;border-radius:50%;background:var(--white);border:2px solid #c9d3e0;display:flex;align-items:center;justify-content:center}
.social span::after{content:"";width:28px;height:28px;border-radius:50%;background:var(--c)}
.copyright{position:absolute;left:7px;bottom:5px;font-size:9.3px;color:var(--white)}
</style>
</head>
<body>
<div class="page">
  <div class="wrap top-strip"></div>
  <header class="wrap header">
    <div class="brand"><span class="brand-dot"></span><span class="brand-name">Vextara</span></div>
    <div class="search">
      <div class="search-field">Search:</div>
      <div class="search-btn"><svg width="16" height="16" viewBox="0 0 16 16"><circle cx="6.5" cy="6.5" r="4.5" fill="none" stroke="#f56a1e" stroke-width="2"/><line x1="10" y1="10" x2="14.5" y2="14.5" stroke="#f56a1e" stroke-width="2.5" stroke-linecap="round"/></svg></div>
    </div>
  </header>
  <nav class="wrap nav">
    <a class="active" href="#">HOME</a><a href="#">WHO WE ARE</a><a href="#">OUR VALUES</a><a href="#">WHAT WE DO</a><a href="#">OUR CLIENTS</a><a href="#">ARTICLES AND PUBLICATIONS</a><a href="#">USEFUL LINKS</a><a href="#">CONTACT US</a>
  </nav>
  <section class="wrap banner">
    <div class="banner-map" role="img" aria-label="Glowing world map with connection lines between business hubs"></div>
    <svg class="arrow prev" viewBox="0 0 30 30"><circle cx="15" cy="15" r="13.5" fill="rgba(20,60,150,.6)" stroke="#4d7fd6" stroke-width="1.5"/><path d="M18 8 L11 15 L18 22" fill="none" stroke="#4d7fd6" stroke-width="2.5"/></svg>
    <svg class="arrow next" viewBox="0 0 30 30"><circle cx="15" cy="15" r="13.5" fill="rgba(20,60,150,.6)" stroke="#4d7fd6" stroke-width="1.5"/><path d="M12 8 L19 15 L12 22" fill="none" stroke="#4d7fd6" stroke-width="2.5"/></svg>
    <ul class="services">
      <li>GOVERNANCE</li><li>GOOD STEWARDSHIP</li><li>FINANCIAL MANAGEMENT INSIGHT</li><li>INFORMATION TECHNOLOGY INSIGHT</li><li>MENTORING AND BUSINESS ADVICE</li>
    </ul>
  </section>
  <section class="wrap welcome">
    <h1>WELCOME</h1>
    <p>Lorem Ipsum is simply dummy text of the printing and typesetting industry. Lorem Ipsum has been the industry's standard dummy text ever since the 1500s, when an unknown printer took a galley of type and scrambled it to make a type specimen book. It has survived not only five centuries, but also the leap into electronic typesetting, remaining essentially unchanged. It was popularised in the 1960s with the release of Letraset sheets containing Lorem Ipsum passages, and more recently with desktop publishing software like Aldus PageMaker including versions of Lorem Ipsum.</p>
    <p>It is a long established fact that a reader will be distracted by the readable content of a page when looking at its layout. The point of using Lorem Ipsum is that it has a more-or-less normal distribution of letters, as opposed to using 'Content here, content here', making it look like readable English. Many desktop publishing packages and web page editors now use Lorem Ipsum as their default model text, and a search for 'lorem ipsum' will uncover many web sites still in their infancy. Various versions have evolved over the years, sometimes by accident, sometimes on purpose (injected humour and the like).</p>
  </section>
  <article class="card" style="left:68px">
    <div class="card-frame"><div class="card-art" role="img" aria-label="Gold figures carrying a large light bulb"></div><div class="card-caption">Our Productive</div></div>
    <p>The standard chunk of Lorem Ipsum used since the 1500s is reproduced below for those interested. Sections 1.10.32 and 1.10.33 from "de Finibus Bonorum et Malorum" by Cicero are also reproduced in their exact original form, accompanied by English versions from the 1914 translation by H. Rackham.</p>
    <a href="#">read more...</a>
  </article>
  <article class="card" style="left:296px">
    <div class="card-frame"><div class="card-art" role="img" aria-label="Gold figures in hard hats measuring with a tape"></div><div class="card-caption">Monitorization</div></div>
    <p>The standard chunk of Lorem Ipsum used since the 1500s is reproduced below for those interested. Sections 1.10.32 and 1.10.33 from "de Finibus Bonorum et Malorum" by Cicero are also reproduced in their exact original form, accompanied by English versions from the 1914 translation by H. Rackham.</p>
    <a href="#">read more...</a>
  </article>
  <article class="card" style="left:524px">
    <div class="card-frame"><div class="card-art" role="img" aria-label="Gold figure stacking rising bar chart blocks"></div><div class="card-caption">Business Growth</div></div>
    <p>The standard chunk of Lorem Ipsum used since the 1500s is reproduced below for those interested. Sections 1.10.32 and 1.10.33 from "de Finibus Bonorum et Malorum" by Cicero are also reproduced in their exact original form, accompanied by English versions from the 1914 translation by H. Rackham.</p>
    <a href="#">read more...</a>
  </article>
  <section class="wrap feature">
    <div class="feature-art" role="img" aria-label="Caliper measuring the word performance"></div>
    <p>There are many variations of passages of Lorem Ipsum available, but the majority have suffered alteration in some form, by injected humour, or randomised words which don't look even slightly believable. If you are going to use a passage of Lorem Ipsum, you need to be sure there isn't anything embarrassing hidden in the middle of text. All the Lorem Ipsum generators on the Internet tend to repeat predefined chunks as necessary, making this the first true generator on the Internet. It uses a dictionary of over 200 Latin words, combined with a handful of model sentence structures, to generate Lorem Ipsum which looks reasonable. The generated Lorem Ipsum is therefore always free from repetition, injected humour, or</p>
  </section>
  <footer class="wrap footer">
    <ul class="foot-links one"><li>Who we are</li><li>Our values</li><li>What we do</li><li>Our Clients</li></ul>
    <ul class="foot-links two"><li>Articles and publications</li><li>Useful links</li><li>Contact us</li><li>Support</li></ul>
    <div class="social" aria-label="Social links">
      <span style="--c:#2aa3e0"></span><span style="--c:#2b55a8"></span><span style="--c:#1f86c4"></span><span style="--c:#d8412f"></span><span style="--c:#d42a26"></span><span style="--c:#f0591c"></span>
    </div>
    <div class="copyright">Copyright © 2014 Vextara Insight Ltd . All right received.</div>
  </footer>
</div>
</body>
</html>
```